KVT Business Cards

We require business cards for our business. We would like a matte black back to the card, with our logo centred in the middle. The front side of the card is open to design.

Target Market(s)

Clients looking for legal services (professional)

Industry/Entity Type

Legal

Contact Information for Business Card

Boris Telemark
Partner
Mobile: 0438 715 642
Email: boris@kvtlaw.co
Website: www.kvtlaw.co
Level 3, 118 Wexbury Street
Sydney NSW 2000

Font styles to use
Other font styles liked:
• Avenir

Colors
f04a50
ffffff
1b1b1b

Requirements
Must have
• Black back with logo included in the centre of the card.
• Our font is Avenir.

```html
<!DOCTYPE html>
<html lang="en">
<head>
<meta charset="utf-8">
<title>KVT Business Cards</title>
<link rel="stylesheet" href="https://fonts.googleapis.com/css2?family=Nunito+Sans:wght@400;600;700;800&display=swap">
<style>
  :root {
    --bg: #2b2b2b;
    --card: #1b1b1b;
    --red: #f04a50;
    --crimson: #c8284a;
    --white: #ffffff;
    --emboss: #272727;
    --emboss-edge: #232323;
  }
  * { margin: 0; padding: 0; box-sizing: border-box; }
  html, body {
    width: 1200px; height: 900px; overflow: hidden;
    background: var(--bg);
    font-family: "Nunito Sans", sans-serif;
  }
  .stage {
    width: 1200px; height: 900px;
    display: flex; flex-direction: column;
    align-items: center; justify-content: center; gap: 40px;
  }
  .card {
    position: relative;
    width: 700px; height: 400px;
    background: var(--card);
    border-radius: 18px;
    box-shadow: 0 12px 30px rgba(0,0,0,0.45);
  }

  /* Brand lockup */
  .brand { position: absolute; display: flex; align-items: center; gap: 22px; }
  .brand-square { width: 74px; height: 74px; }
  .brand-name {
    font-weight: 800; font-size: 30px; line-height: 1.0;
    letter-spacing: 0.5px; text-transform: uppercase;
  }

  /* Back */
  .card-back .brand { left: 50%; top: 118px; transform: translateX(-50%); }
  .card-back .brand-square { background: var(--emboss); box-shadow: inset 0 0 0 1px var(--emboss-edge); }
  .card-back .brand-name { color: var(--emboss); }
  .back-web {
    position: absolute; left: 0; right: 0; top: 286px;
    text-align: center; color: var(--red);
    font-size: 15px; letter-spacing: 1.5px; font-weight: 600;
  }

  /* Front */
  .card-front .brand { left: 270px; top: 82px; }
  .card-front .brand-square { background: var(--crimson); }
  .card-front .brand-name { color: var(--white); }

  .contact {
    position: absolute; right: 38px; top: 180px;
    list-style: none; text-align: right;
    color: var(--white); font-size: 16px; letter-spacing: 0.6px; line-height: 25px;
  }
  .contact li { display: flex; justify-content: flex-end; align-items: center; gap: 10px; }
  .contact svg { width: 13px; height: 13px; fill: var(--red); }

  .person { position: absolute; left: 48px; bottom: 44px; color: var(--white); }
  .person-name { color: var(--crimson); font-size: 25px; font-weight: 700; letter-spacing: 0.5px; }
  .person-role { font-size: 18px; font-weight: 600; margin-top: 2px; }
  .person-rule { width: 70px; height: 2px; background: var(--crimson); margin: 8px 0 10px; }
  .person-address { font-style: normal; font-size: 15px; line-height: 21px; letter-spacing: 0.4px; }
</style>
</head>
<body>
<main class="stage">

  <section class="card card-back" aria-label="Card back">
    <div class="brand">
      <span class="brand-square"></span>
      <span class="brand-name">Kerrow<br>Vale<br>Telemark</span>
    </div>
    <p class="back-web">www.kvtlaw.co</p>
  </section>

  <section class="card card-front" aria-label="Card front">
    <div class="brand">
      <span class="brand-square"></span>
      <span class="brand-name">Kerrow<br>Vale<br>Telemark</span>
    </div>

    <ul class="contact">
      <li>0438 715 642
        <svg viewBox="0 0 24 24" aria-hidden="true"><path d="M6.6 10.8a15.1 15.1 0 0 0 6.6 6.6l2.2-2.2a1 1 0 0 1 1-.25 11.4 11.4 0 0 0 3.6.57 1 1 0 0 1 1 1V20a1 1 0 0 1-1 1A17 17 0 0 1 3 4a1 1 0 0 1 1-1h3.5a1 1 0 0 1 1 1c0 1.25.2 2.45.57 3.57a1 1 0 0 1-.25 1z"/></svg>
      </li>
      <li>boris@kvtlaw.co
        <svg viewBox="0 0 24 24" aria-hidden="true"><path d="M2 5h20v14H2z M4 7v.5l8 5 8-5V7l-8 5z"/></svg>
      </li>
      <li>www.kvtlaw.co
        <svg viewBox="0 0 24 24" aria-hidden="true"><path d="M12 2a10 10 0 1 0 0 20 10 10 0 0 0 0-20zm6.9 6h-3a15.7 15.7 0 0 0-1.4-3.6A8 8 0 0 1 18.9 8zM12 4c.8 1.2 1.5 2.5 1.9 4h-3.8c.4-1.5 1.1-2.8 1.9-4zM4.3 14a8 8 0 0 1 0-4h3.4a16.5 16.5 0 0 0 0 4zm.8 2h3a15.7 15.7 0 0 0 1.4 3.6A8 8 0 0 1 5.1 16zM8 8H5.1a8 8 0 0 1 4.4-3.6C8.9 5.5 8.4 6.7 8 8zm4 12c-.8-1.2-1.5-2.5-1.9-4h3.8c-.4 1.5-1.1 2.8-1.9 4zm2.3-6H9.7a14.7 14.7 0 0 1 0-4h4.6a14.7 14.7 0 0 1 0 4zm.2 5.6c.6-1.1 1.1-2.3 1.4-3.6h3a8 8 0 0 1-4.4 3.6zm1.8-5.6a16.5 16.5 0 0 0 0-4h3.4a8 8 0 0 1 0 4z"/></svg>
      </li>
    </ul>

    <div class="person">
      <p class="person-name">Boris Telemark</p>
      <p class="person-role">Partner</p>
      <div class="person-rule"></div>
      <address class="person-address">Level 3, 118 Wexbury Street<br>Sydney NSW 2000</address>
    </div>
  </section>

</main>
</body>
</html>
```